The amber lantern with an elephant incorporated in the background

Target Market(s)

Real estate

Industry/Entity Type

Real Estate

Contact Information for Business Card

On back on want my name & number
In front I want the business name, "the amber lantern", below to say staging & design

Logo Text

The amber lantern

Font styles to use
Serif

Colors
000000

Requirements
Must have
• I want an elephant behind the writing in gold transperant

```html
<!DOCTYPE html>
<html lang="en">
<head>
<meta charset="utf-8">
<title>The Amber Lantern — Business Cards</title>
<link rel="stylesheet" href="https://fonts.googleapis.com/css2?family=Open+Sans:wght@400;600&family=Didact+Gothic&display=swap">
<style>
  :root {
    --gold: #dfb217;
    --paper: #ffffff;
    --backdrop: #ecebe8;
    --rule: #c9b469;
    --grey: #6f6f6f;
    --rule-grey: #8a8a8a;
  }
  * { margin: 0; padding: 0; box-sizing: border-box; }
  html, body { width: 1200px; height: 900px; overflow: hidden; }
  body {
    position: relative;
    background: var(--backdrop);
    font-family: "Open Sans", Arial, sans-serif;
  }
  .card {
    position: absolute;
    box-shadow: 0 6px 18px rgba(0,0,0,0.12);
    overflow: hidden;
  }
  /* Contact side */
  .card--contact {
    left: 238px; top: 62px; width: 555px; height: 343px;
    background: var(--gold);
    color: var(--paper);
  }
  .contact-side__band {
    position: absolute; right: 0; top: 0;
    width: 150px; height: 100%;
    background: var(--paper);
  }
  .contact-side__mark {
    position: absolute; left: 300px; top: 10px;
    width: 235px; height: 235px; border-radius: 50%;
    background: var(--gold);
    border: 6px solid var(--paper);
  }
  .contact-name {
    position: absolute; left: 32px; top: 106px;
    font-weight: 600; font-size: 20px; letter-spacing: 0.1px;
  }
  .contact-address {
    position: absolute; left: 33px; top: 145px;
    font-size: 14px; line-height: 17px;
  }
  .contact-list {
    position: absolute; left: 33px; top: 203px;
    list-style: none; font-size: 14px; line-height: 23px;
  }
  .contact-list li { display: flex; align-items: center; gap: 6px; }
  .contact-list svg { width: 11px; height: 11px; fill: var(--paper); }

  /* Brand side */
  .card--brand {
    left: 457px; top: 518px; width: 560px; height: 344px;
    background: var(--paper);
    font-family: "Didact Gothic", "Century Gothic", sans-serif;
    text-align: center;
  }
  .brand-mark {
    position: absolute; left: 228px; top: 58px;
    width: 104px; height: 104px; border-radius: 50%;
    background: var(--gold);
  }
  .brand-article {
    position: absolute; left: 0; right: 0; top: 207px;
    display: flex; align-items: center; justify-content: center; gap: 12px;
    color: var(--gold); font-size: 18px; letter-spacing: 1px;
  }
  .brand-article::before, .brand-article::after {
    content: ""; width: 138px; height: 1px; background: var(--rule);
  }
  .brand-name {
    position: absolute; left: 0; right: 0; top: 231px;
    color: var(--gold); font-size: 33px; letter-spacing: 0.5px;
  }
  .brand-tagline {
    position: absolute; left: 0; right: 0; top: 273px;
    display: flex; align-items: center; justify-content: center; gap: 10px;
    color: var(--grey); font-size: 14px; letter-spacing: 1.5px;
  }
  .brand-tagline::before, .brand-tagline::after {
    content: ""; width: 70px; height: 1px; background: var(--rule-grey);
  }
</style>
</head>
<body>
  <section class="card card--contact" aria-label="Contact side">
    <div class="contact-side__band"></div>
    <div class="contact-side__mark"></div>
    <h1 class="contact-name">Marlowe Finch</h1>
    <p class="contact-address">48 Harbor Lane, Suite 2<br>Westbrook, 204518</p>
    <ul class="contact-list">
      <li>
        <svg viewBox="0 0 24 24" aria-hidden="true"><path d="M6.6 10.8c1.4 2.8 3.8 5.1 6.6 6.6l2.2-2.2c.3-.3.7-.4 1-.2 1.1.4 2.3.6 3.6.6.6 0 1 .4 1 1V20c0 .6-.4 1-1 1C10.6 21 3 13.4 3 4c0-.6.4-1 1-1h3.5c.6 0 1 .4 1 1 0 1.2.2 2.4.6 3.6.1.3 0 .7-.2 1z"/></svg>
        (052)-318-4476
      </li>
      <li>
        <svg viewBox="0 0 24 24" aria-hidden="true"><path d="M2 5h20v14H2z M2 5l10 8 10-8" fill="none" stroke="#fff" stroke-width="0"/><path d="M2 6v13h20V6l-10 7.5z M2.5 5h19L12 12z"/></svg>
        hello@amberlantern.co
      </li>
    </ul>
  </section>

  <section class="card card--brand" aria-label="Brand side">
    <div class="brand-mark"></div>
    <div class="brand-article">THE</div>
    <div class="brand-name">AMBER LANTERN</div>
    <div class="brand-tagline">STAGING &amp; DESIGN</div>
  </section>
</body>
</html>
```